Business Card Design

The new Company is called The Gilded Pecan - based in Miami Beach, Florida and Connecticut. We want a business card to be catchy and memorable ( like our Company name). Our business is marketing and retail sales of flavored cashew nuts in boutique /high end stores. The new business card must include a logo which must be a cashew nut with a king's crown or Roman wreath.
Yes- we are looking for a logo to be designed for the business and for the business card.

Industry/Entity Type

Marketing

Font styles to use
Script

```html
<!DOCTYPE html>
<html lang="en">
<head>
<meta charset="utf-8">
<title>The Gilded Pecan – Business Card</title>
<link rel="stylesheet" href="https://fonts.googleapis.com/css2?family=Courgette&display=swap">
<style>
  :root {
    --canvas: #ffffff;
    --card: #ffffff;
    --card-edge: #5a5a5a;
    --tan: #d4b486;
    --ink: #2f2f2f;
    --nut-light: #e8cfa0;
    --nut-mid: #c9a472;
    --nut-dark: #8a6a42;
  }
  html, body {
    margin: 0;
    padding: 0;
    width: 1200px;
    height: 1000px;
    overflow: hidden;
    background: var(--canvas);
  }
  .stage {
    position: relative;
    width: 1200px;
    height: 1000px;
  }
  .business-card {
    position: absolute;
    left: 50px;
    top: 173px;
    width: 1100px;
    height: 653px;
    display: block;
  }
  .card-text {
    font-family: "Courgette", cursive;
    fill: var(--ink);
  }
  .brand-name { font-size: 58px; }
  .holder-name { font-size: 33px; }
  .contact-line { font-size: 21px; }
  .contact-phone { font-size: 23px; }
  .website { font-size: 20px; }
</style>
</head>
<body>
<main class="stage">
  <svg class="business-card" viewBox="0 0 918 545" xmlns="http://www.w3.org/2000/svg">
    <defs>
      <linearGradient id="cashew-tones" x1="0" y1="0" x2="1" y2="1">
        <stop offset="0" stop-color="var(--nut-light)"/>
        <stop offset="0.55" stop-color="var(--nut-mid)"/>
        <stop offset="1" stop-color="var(--nut-dark)"/>
      </linearGradient>
    </defs>

    <rect class="card-stock" x="0.5" y="0.5" width="917" height="544" fill="var(--card)" stroke="var(--card-edge)" stroke-width="1"/>

    <rect class="header-band" x="12" y="15" width="890" height="214" fill="var(--tan)"/>

    <rect class="lower-field" x="12" y="244" width="890" height="281" fill="var(--tan)"/>

    <rect class="photo-frame" x="74" y="229" width="388" height="220" fill="var(--card)"/>
    <rect class="product-photo" x="83" y="244" width="370" height="203" fill="url(#cashew-tones)"
          role="img" aria-label="Photograph of roasted cashew nuts piled together"/>
    <path class="photo-wave" d="M74,405 C160,372 262,384 340,418 C392,440 430,449 462,445 L462,462 L74,462 Z" fill="var(--tan)"/>

    <rect class="contact-panel" x="521" y="229" width="381" height="241" fill="var(--card)"/>
    <path class="contact-curve" d="M902,315 C852,418 726,472 600,470 L902,470 Z" fill="var(--tan)"/>

    <circle class="brand-dot" cx="480" cy="80" r="26" fill="var(--ink)"/>
    <text class="card-text brand-name" x="480" y="180" text-anchor="middle">The Gilded Pecan</text>

    <text class="card-text holder-name" x="710" y="266" text-anchor="middle">Your name</text>
    <text class="card-text contact-line" x="581" y="301">Street Address</text>
    <text class="card-text contact-line" x="579" y="340">City,State and Country</text>
    <text class="card-text contact-line" x="579" y="371">sales@gpecan.com</text>
    <text class="card-text contact-line" x="579" y="405">Phone</text>
    <text class="card-text contact-phone" x="577" y="432">305-555-0142</text>

    <text class="card-text website" x="895" y="515" text-anchor="end">www.gildedpecan.com</text>
  </svg>
</main>
</body>
</html>
```